Tallwren Learning Graphic Design Project

I need graphic design elements to establish a look and feel for my company, Tallwren Learning. I work with companies and organizations who are either starting out in eLearning and need direction or have been at it for a while and could do it better. I work inside the organization to analyse their current learning, devise strategic plans and then stay around to help implement them. This saves the organization a lot of money and gives them happier and more able workers.
I have been working in this industry for many years and see the need for a very specific consultancy focused on the strategies behind adult learning offerings that involve screens (this is almost all).
Tallwren thinks outside the box. But it also follows up with concrete results. Surprising things can be achieved. This is the kind of feeling I'd like to convey in the Tallwren look and feel. So I'm looking for a set of graphic elements that can be used mainly for business cards and website objects. To give you an idea of the style of thing I like I have attached a business card template that I like. What I like is its freshness and clarity. But open to all ideas. Thanks and good luck.
Updates

 I've posted a new image  to show what I mean by clean and fresh. Not suggesting that I need a cord with a knot in it but I really like the colour, contrast and sort of starkness of the image. Suggesting this as apossible direction change to use with those good ideas already submitted and to help clarify for new ones. Thanks again.

                                   

Target Market(s)

corporates and larger organizations - any organization that has or wants to have elearning in their training mix.

Industry/Entity Type

Graphic Design

Requirements
Must have
• elements that can be used to create a website, business cards, other materials as required. So this might include a font recommendation and a number of illustrations that can be used together or separately.
Nice to have
• nice if you could include the elements designed as a business card in a ready-to-print format.
Should not have
• don't really want a logo in the usual sense

```html
<!DOCTYPE html>
<html lang="en">
<head>
<meta charset="utf-8">
<title>Tallwren Learning – Business Cards</title>
<link rel="stylesheet" href="https://fonts.googleapis.com/css2?family=Quicksand:wght@400;500&display=swap">
<style>
  :root {
    --page-bg: #e9e6e1;
    --card-blue: #4aa9df;
    --card-white: #ffffff;
    --text-light: #ffffff;
    --swirl-orange: rgba(240, 122, 42, 0.55);
    --swirl-pink: rgba(217, 74, 154, 0.40);
    --swirl-yellow: rgba(245, 189, 46, 0.35);
    --swirl-navy: rgba(31, 93, 156, 0.12);
    --fade: rgba(255, 255, 255, 0);
  }
  * { box-sizing: border-box; margin: 0; padding: 0; }
  html, body {
    width: 1200px;
    height: 720px;
    overflow: hidden;
    background: var(--page-bg);
    font-family: "Quicksand", sans-serif;
  }
  .canvas {
    position: relative;
    width: 1200px;
    height: 720px;
  }
  .card {
    position: absolute;
    top: 212px;
    width: 520px;
    height: 296px;
    box-shadow: 0 6px 18px rgba(0, 0, 0, 0.18);
    overflow: hidden;
  }
  .card--front { left: 60px; background: var(--card-blue); }
  .card--back  { left: 620px; background: var(--card-white); }

  .swirl-area { position: absolute; }
  .card--front .swirl-area {
    left: 250px;
    top: 4px;
    width: 266px;
    height: 196px;
    background: radial-gradient(closest-side,
      var(--swirl-orange) 0%,
      var(--swirl-pink) 40%,
      var(--swirl-yellow) 68%,
      rgba(74, 169, 223, 0) 100%);
  }
  .card--back .swirl-area {
    left: 110px;
    top: 4px;
    width: 320px;
    height: 288px;
    background: radial-gradient(closest-side,
      var(--swirl-orange) 0%,
      var(--swirl-pink) 35%,
      var(--swirl-yellow) 62%,
      var(--swirl-navy) 82%,
      var(--fade) 100%);
  }

  .card__text {
    position: absolute;
    left: 28px;
    bottom: 26px;
    color: var(--text-light);
  }
  .card__name {
    font-size: 27px;
    font-weight: 500;
    letter-spacing: 0.5px;
  }
  .card__tagline {
    margin-top: 4px;
    font-size: 17px;
    font-style: italic;
    letter-spacing: 0.6px;
  }
  .card__web {
    margin-top: 30px;
    font-size: 17px;
    letter-spacing: 0.8px;
  }
</style>
</head>
<body>
  <main class="canvas">
    <section class="card card--front" aria-label="Business card front">
      <div class="swirl-area" role="img" aria-label="Multicoloured looping line pattern in orange, pink, yellow, green and navy"></div>
      <div class="card__text">
        <p class="card__name">Tallwren Learning</p>
        <p class="card__tagline">never stop creating, never stop learning</p>
        <p class="card__web">www.tallwren.net.au</p>
      </div>
    </section>
    <section class="card card--back" aria-label="Business card back">
      <div class="swirl-area" role="img" aria-label="Multicoloured wave of looping lines running diagonally across the card"></div>
    </section>
  </main>
</body>
</html>
```